Corwin Crest Homes Needs Business Card Design

Looking for a unique modern business card to fit my new Logo.
Name: Marcus Corwin
Company: Corwin Crest Homes, LLC
Tag Line: Built To Stand Firm
Email: corwincresthomes@mailnest.example
Phone: (555) 017-2846
Website: www.corwincresthomes.example
License: CORWICH462KX

```html
<!DOCTYPE html>
<html lang="en">
<head>
<meta charset="utf-8">
<title>Corwin Crest Homes — Business Card</title>
<link href="https://fonts.googleapis.com/css2?family=Montserrat:wght@500;700;800&family=Mulish:wght@500;600&display=swap" rel="stylesheet">
<style>
  :root {
    --page-bg: #d9d9d7;
    --card-bg: #202020;
    --pattern-light: #262626;
    --pattern-dark: #1b1b1b;
    --brand-blue: #2f8fd6;
    --text-white: #f4f4f4;
    --card-shadow: 0 18px 40px rgba(0, 0, 0, 0.35);
  }
  * { margin: 0; padding: 0; box-sizing: border-box; }
  html, body {
    width: 1200px;
    height: 900px;
    overflow: hidden;
    background: var(--page-bg);
  }
  .canvas {
    position: relative;
    width: 1200px;
    height: 900px;
  }
  .card {
    position: absolute;
    width: 700px;
    height: 400px;
    border-radius: 26px;
    background: var(--card-bg);
    box-shadow: var(--card-shadow);
    overflow: hidden;
  }
  .card--back { left: 140px; top: 35px; }
  .card--front { left: 360px; top: 465px; }

  /* Back side */
  .back-pattern {
    position: absolute;
    inset: 0;
    background: linear-gradient(135deg, var(--pattern-light), var(--pattern-dark));
  }
  .back-brand {
    position: absolute;
    right: 60px;
    top: 172px;
    display: flex;
    align-items: center;
    gap: 34px;
  }
  .tagline {
    font-family: "Montserrat", sans-serif;
    font-weight: 500;
    font-size: 27px;
    letter-spacing: 0.2em;
    color: var(--brand-blue);
    text-transform: uppercase;
    white-space: nowrap;
  }
  .back-brand__name {
    font-family: "Montserrat", sans-serif;
    font-weight: 700;
    font-size: 17px;
    line-height: 1.15;
    color: var(--brand-blue);
    text-transform: uppercase;
    letter-spacing: 0.04em;
  }

  /* Front side */
  .front-brand {
    position: absolute;
    right: 56px;
    top: 52px;
    display: flex;
    align-items: center;
    gap: 14px;
  }
  .front-brand__mark {
    width: 16px;
    height: 16px;
    background: var(--brand-blue);
  }
  .front-brand__name {
    font-family: "Montserrat", sans-serif;
    font-weight: 800;
    font-size: 28px;
    letter-spacing: 0.02em;
    color: var(--text-white);
    text-transform: uppercase;
  }
  .contact-block {
    position: absolute;
    left: 56px;
    bottom: 44px;
  }
  .person-name {
    font-family: "Montserrat", sans-serif;
    font-weight: 800;
    font-size: 36px;
    color: var(--brand-blue);
    text-transform: uppercase;
    line-height: 1;
  }
  .license {
    font-family: "Mulish", sans-serif;
    font-weight: 600;
    font-size: 20px;
    color: var(--text-white);
    margin-top: 8px;
  }
  .contact-list {
    list-style: none;
    margin-top: 22px;
    display: flex;
    flex-direction: column;
    gap: 8px;
  }
  .contact-list__item {
    display: flex;
    align-items: center;
    gap: 12px;
    font-family: "Mulish", sans-serif;
    font-weight: 500;
    font-size: 20px;
    color: var(--text-white);
  }
  .contact-list__icon {
    width: 18px;
    height: 18px;
    flex: none;
  }
</style>
</head>
<body>
<main class="canvas">

  <section class="card card--back" aria-label="Card back">
    <div class="back-pattern" role="img" aria-label="Embossed repeating brand pattern in tone-on-tone black"></div>
    <div class="back-brand">
      <p class="tagline">Built To Stand Firm</p>
      <p class="back-brand__name">Corwin<br>Crest</p>
    </div>
  </section>

  <section class="card card--front" aria-label="Card front">
    <div class="front-brand">
      <span class="front-brand__mark"></span>
      <p class="front-brand__name">Corwin Crest Homes</p>
    </div>

    <div class="contact-block">
      <h1 class="person-name">Marcus Corwin</h1>
      <p class="license">License: CORWICH462KX</p>
      <ul class="contact-list">
        <li class="contact-list__item">
          <svg class="contact-list__icon" viewBox="0 0 24 24" aria-hidden="true">
            <path fill="#2f8fd6" d="M6.6 10.8a15.1 15.1 0 0 0 6.6 6.6l2.2-2.2a1 1 0 0 1 1-.25 11.4 11.4 0 0 0 3.6.57 1 1 0 0 1 1 1V20a1 1 0 0 1-1 1A17 17 0 0 1 3 4a1 1 0 0 1 1-1h3.5a1 1 0 0 1 1 1c0 1.25.2 2.45.57 3.57a1 1 0 0 1-.25 1z"/>
          </svg>
          (555) 017-2846
        </li>
        <li class="contact-list__item">
          <svg class="contact-list__icon" viewBox="0 0 24 24" aria-hidden="true">
            <rect x="2" y="5" width="20" height="14" rx="2" fill="#2f8fd6"/>
            <path d="M3 6l9 7 9-7" fill="none" stroke="#202020" stroke-width="1.8"/>
          </svg>
          corwincresthomes@mailnest.example
        </li>
        <li class="contact-list__item">
          <svg class="contact-list__icon" viewBox="0 0 24 24" aria-hidden="true">
            <g fill="none" stroke="#2f8fd6" stroke-width="1.8">
              <circle cx="12" cy="12" r="9.5"/>
              <ellipse cx="12" cy="12" rx="4" ry="9.5"/>
              <path d="M2.5 12h19M4 7h16M4 17h16"/>
            </g>
          </svg>
          www.corwincresthomes.example
        </li>
      </ul>
    </div>
  </section>

</main>
</body>
</html>
```